Ophthalmic device company needs packaging modernization

We are medical device company that needs a new look for their packaging design. It should look clean and sophisticated. The logo must not be changed. Please maintain the branding of the logo.

Refer to the attached product brochure for the product specifications and the packaging template we want designed.

The box design should fit within our branding style which you can view at www.kelvarn.com

Please message me if anything is unclear.

Target Market(s)

Eye Surgeons, eye surgery patients

Industry/Entity Type

It Company

```html
<!DOCTYPE html>
<html lang="en">
<head>
<meta charset="utf-8">
<title>Kelvarn 620UV Packaging</title>
<link rel="stylesheet" href="https://fonts.googleapis.com/css2?family=Open+Sans:wght@300;400;600;700&family=Montserrat:wght@400;500&display=swap">
<style>
  :root {
    --stage: #d4d4d4;
    --white: #ffffff;
    --crimson: #d31f45;
    --charcoal: #4a4a4a;
    --ink: #3a3a3a;
    --muted: #8a8a8a;
    --lens-light: #f1f4f6;
    --lens-mid: #d2dbe1;
  }
  * { box-sizing: border-box; margin: 0; padding: 0; }
  html, body { width: 1040px; height: 1200px; overflow: hidden; }
  body {
    background: var(--stage);
    font-family: "Open Sans", Arial, sans-serif;
    color: var(--ink);
    position: relative;
  }
  .box-face {
    position: absolute;
    left: 134px;
    width: 772px;
    height: 540px;
    background: var(--white);
    overflow: hidden;
  }
  .box-face.front { top: 40px; }
  .box-face.back { top: 620px; }

  .header {
    position: absolute; left: 0; top: 0; width: 100%; height: 124px;
    display: flex; align-items: center; justify-content: space-between;
    padding: 0 56px 0 32px;
  }
  .brand {
    display: flex; align-items: center; gap: 10px;
    font-family: "Montserrat", Arial, sans-serif;
    font-weight: 500; font-size: 36px; color: var(--crimson);
    letter-spacing: 0.5px;
  }
  .brand-dot {
    width: 16px; height: 16px; border-radius: 50%;
    background: var(--charcoal);
  }
  .tagline {
    font-family: "Montserrat", Arial, sans-serif;
    font-size: 19px; letter-spacing: 7px; color: var(--muted);
    white-space: nowrap;
  }

  /* front */
  .front .title-panel {
    position: absolute; left: 0; top: 124px; width: 356px; height: 281px;
    background: var(--crimson); color: var(--white);
    padding: 82px 0 0 28px;
  }
  .model-name { font-weight: 300; font-size: 80px; line-height: 1; letter-spacing: 2px; }
  .model-type { font-weight: 300; font-size: 28px; margin-top: 8px; }
  .front .lens-panel {
    position: absolute; left: 356px; top: 124px; width: 416px; height: 281px;
    background: linear-gradient(180deg, #fafafa, #eeeeee);
  }
  .front .lens-art {
    position: absolute; left: 70px; top: 18px; width: 220px; height: 240px;
  }
  .lens-art {
    border-radius: 50%;
    background: radial-gradient(circle at 45% 40%, var(--lens-light), var(--lens-mid));
  }
  .line-name {
    position: absolute; right: 20px; bottom: 10px; text-align: right;
    font-weight: 700; font-size: 34px; color: var(--ink);
  }
  .line-name span { display: block; font-size: 13px; font-weight: 600; margin-top: -4px; }
  .front .footer {
    position: absolute; left: 0; top: 405px; width: 100%; height: 135px;
    background: var(--charcoal); color: var(--white);
    padding: 24px 28px;
  }
  .material { font-weight: 600; font-size: 17px; }
  .material-sub { font-size: 15px; letter-spacing: 0.5px; }
  .caution {
    display: inline-block; margin-top: 20px;
    border: 1px solid var(--white); padding: 4px 8px; font-size: 12px;
  }

  /* back */
  .back .advantage-panel {
    position: absolute; left: 0; top: 124px; width: 312px; height: 416px;
    background: var(--crimson); color: var(--white);
    padding: 26px 14px 0 28px;
  }
  .advantage-title {
    font-family: "Montserrat", Arial, sans-serif;
    font-weight: 400; font-size: 14px; letter-spacing: 2px;
    white-space: nowrap; margin-bottom: 12px;
  }
  .advantage-list { list-style: none; width: 258px; }
  .advantage-list li {
    font-size: 16px; line-height: 1.1;
    padding: 6px 0 7px; border-bottom: 1px solid rgba(255,255,255,0.75);
  }
  .advantage-list li:last-child { border-bottom: none; }
  .contents {
    position: absolute; left: 336px; top: 160px; width: 260px;
  }
  .contents h2 { font-size: 19px; font-weight: 600; margin-bottom: 28px; }
  .contents li { list-style: none; font-size: 19px; line-height: 1.25; white-space: nowrap; }
  .back .lens-art {
    position: absolute; left: 612px; top: 166px; width: 110px; height: 160px;
  }
  .back .lens-edge {
    position: absolute; left: 738px; top: 158px; width: 6px; height: 170px;
    border-radius: 3px; background: linear-gradient(90deg, var(--lens-mid), var(--lens-light));
  }
  .back .footer {
    position: absolute; left: 312px; top: 400px; width: 460px; height: 140px;
    background: var(--charcoal); color: var(--white);
    padding: 16px 30px 0 0; text-align: right;
    font-size: 19px; line-height: 1.25;
  }
  .back .footer .web { margin-top: 6px; }
</style>
</head>
<body>
  <section class="box-face front">
    <header class="header">
      <div class="brand"><span class="brand-dot"></span>KELVARN</div>
      <div class="tagline">CLEAR SIGHT FORWARD</div>
    </header>
    <div class="title-panel">
      <h1 class="model-name">620UV</h1>
      <p class="model-type">HYDROPHOBIC LENS</p>
    </div>
    <div class="lens-panel">
      <div class="lens-art" role="img" aria-label="Intraocular lens with curved haptics"></div>
      <p class="line-name">Claraform<span>360° Square Edge</span></p>
    </div>
    <div class="footer">
      <p class="material">NATURAL YELLOW HYDROPHOBIC ACRYLIC</p>
      <p class="material-sub">FOLDABLE INTRAOCULAR LENS</p>
      <p class="caution">CAUTION: Federal law restricts this device to sale by or on the order of a physician.</p>
    </div>
  </section>

  <section class="box-face back">
    <header class="header">
      <div class="brand"><span class="brand-dot"></span>KELVARN</div>
      <div class="tagline">CLEAR SIGHT FORWARD</div>
    </header>
    <div class="advantage-panel">
      <h2 class="advantage-title">THE KELVARN ADVANTAGE</h2>
      <ul class="advantage-list">
        <li>Offers superior optical centering properties</li>
        <li>Reduces PCO</li>
        <li>360° square edge</li>
        <li>Edge profile to reduce dysphotopsia on frontside</li>
        <li>Unfold time less than 10 seconds</li>
        <li>Foldable hydrophobic acrylate with UV blocker</li>
        <li>Glistening free optics</li>
      </ul>
    </div>
    <div class="contents">
      <h2>CONTENTS:</h2>
      <ul>
        <li>One Sterile Intraocular Lens</li>
        <li>One Patient ID Card</li>
        <li>One Product Insert</li>
        <li>One Record Label Sheet</li>
      </ul>
    </div>
    <div class="lens-art" role="img" aria-label="Intraocular lens front view"></div>
    <div class="lens-edge" role="img" aria-label="Intraocular lens side profile"></div>
    <div class="footer">
      <p>1840 Harrow Mill Road, Dunmore,<br>Ohio 43210 USA</p>
      <p class="web">hello@kelvarn.com<br>www.kelvarn.com</p>
    </div>
  </section>
</body>
</html>
```